Spa needs a highly desired Membership Card

We need a membership card that captures people's desire to own it(our membership) when flashed by anyone! It should tell the "class" of the card owner!
Comes in Silver & Gold membership. Wants to have same design in different colour/tone to differentiate Gold & Silver.
Most members are woman, but we have few men as well.
Updates
Hi Designers,
Target Market(s)
Woman age 25-55 years old. High spending power in a relatively poor country(Myanmar).
They may be rich businesswomen, wives/daughters of rich man, women who are educated abroad and now return to home country as Myanmar is fast developing.
Requirements
Must have
- Must be in tiff, bmp or jpeg format so that card printer can recognise.
- TEXT
- Velmora Spa (font: Monotype Corsiva)
- No 18, Kethin Street, Sula Court (Level-2) (4117), Dagon Township, Yangon
- 09 47268031
- contactus@ternwick-holdco.example
- A space for picture of card owner.
- No magnetic strip/smart chip.
- Name Abcdefghijklmn
- Membership No 12345678
- Expiry MM/YYYY
- For Gold:
- Terms and Conditions
- - Members enjoy 25% off all standard services, excluding promotional offers
- - Members enjoy 5% off for Quessaline products, excluding promotional items
- - Members enjoy 10% off for all other retail products, excluding promotional items
- - 1 accompanying guest in a day enjoys 20% off standard services, excluding promotional offers
- - Memberships are valid for 2 years from the date of issue and are non-transferable
- - Memberships sold are non-refundable or exchangeable for cash, services or products
- - Privileges are subject to change without prior notice
- For Silver:
- Terms and Conditions
- - Members enjoy 20% off all standard services, excluding promotional offers
- I uploaded 2 of our spa pictures so you can have a feel our of premise. And uploaded our name card, I agree its not stylish as I designed it myself.

```html
<!DOCTYPE html>
<html lang="en">
<head>
<meta charset="utf-8">
<title>Velmora Spa – Exclusive VIP Cards</title>
<link rel="stylesheet" href="https://fonts.googleapis.com/css2?family=Arimo:ital,wght@0,700;1,400&display=swap">
<style>
  :root {
    --page-bg: #ebebeb;
    --card-bg: #ffffff;
    --card-top: #e9ebef;
    --brand-grey: #5a5a5a;
    --label-grey: #6b6b6b;
    --gold-dark: #8f600e;
    --gold-mid: #d2a033;
    --gold-light: #f5dc8c;
    --silver-dark: #8a8a8a;
    --silver-mid: #c9c9c9;
    --silver-light: #f8f8f8;
    --silver-text: #4a4a4a;
    --ribbon-white: #ffffff;
    --glow: rgba(255, 214, 170, 0.85);
    --rb-red: #e8283c;
    --rb-pink: #ee5fa0;
    --rb-orange: #f59a2a;
    --rb-yellow: #f1d43a;
    --rb-green: #3fbf5a;
    --rb-blue: #3c8fe0;
    --rb-violet: #9a5ad6;
  }
  * { box-sizing: border-box; margin: 0; padding: 0; }
  html, body {
    width: 1200px; height: 1000px; overflow: hidden;
    background: var(--page-bg);
  }
  .stage { position: relative; width: 1200px; height: 1000px; }

  .vip-card {
    position: absolute;
    width: 620px; height: 395px;
    border-radius: 16px;
    background:
      radial-gradient(ellipse 38% 14% at 62% 6%, var(--glow), transparent 70%),
      linear-gradient(180deg, var(--card-top) 0%, var(--card-bg) 34%, var(--card-bg) 100%);
    box-shadow: 0 6px 14px rgba(0, 0, 0, 0.22);
    overflow: hidden;
  }
  .vip-card--gold { left: 105px; top: 85px; }
  .vip-card--silver { left: 400px; top: 490px; }

  /* flowing rainbow line artwork, shown as a soft gradient field */
  .card-art { position: absolute; inset: 0; }
  .art-swirl {
    position: absolute; left: 300px; top: 0; width: 320px; height: 300px;
    background: linear-gradient(115deg, var(--rb-pink) 0%, var(--rb-red) 22%, var(--rb-orange) 38%, var(--rb-yellow) 50%, var(--rb-green) 62%, var(--rb-blue) 80%, var(--rb-violet) 100%);
    -webkit-mask-image: radial-gradient(ellipse 48% 50% at 55% 50%, #000 25%, transparent 75%);
    mask-image: radial-gradient(ellipse 48% 50% at 55% 50%, #000 25%, transparent 75%);
    opacity: 0.7;
  }
  .art-band {
    position: absolute; left: 0; top: 215px; width: 620px; height: 120px;
    background: linear-gradient(90deg, var(--rb-blue) 0%, var(--rb-green) 22%, var(--rb-yellow) 38%, var(--rb-orange) 52%, var(--rb-red) 70%, var(--rb-pink) 100%);
    -webkit-mask-image: radial-gradient(ellipse 55% 45% at 50% 45%, #000 15%, transparent 75%);
    mask-image: radial-gradient(ellipse 55% 45% at 50% 45%, #000 15%, transparent 75%);
    opacity: 0.45;
  }

  .brand {
    position: absolute; left: 40px; top: 72px;
    display: flex; align-items: center; gap: 10px;
  }
  .brand-dot {
    width: 30px; height: 30px; border-radius: 50%;
    background: var(--brand-grey);
  }
  .brand-name {
    font-family: "Arimo", sans-serif;
    font-weight: 700; font-size: 26px;
    color: var(--brand-grey);
  }

  .tier-ribbon {
    position: absolute; left: 0; top: 168px;
    width: 452px; height: 56px;
    clip-path: polygon(0 0, 95% 0, 100% 50%, 95% 100%, 0 100%);
    display: flex; align-items: center; gap: 8px;
    padding-left: 24px;
  }
  .vip-card--gold .tier-ribbon {
    background: linear-gradient(90deg, var(--gold-dark) 0%, var(--gold-mid) 35%, var(--gold-light) 55%, var(--gold-mid) 75%, var(--gold-dark) 100%);
    color: var(--ribbon-white);
  }
  .vip-card--silver .tier-ribbon {
    background: linear-gradient(90deg, var(--silver-mid) 0%, var(--silver-light) 40%, var(--silver-mid) 70%, var(--silver-dark) 100%);
    color: var(--silver-text);
  }
  .tier-name {
    font-family: "Arimo", sans-serif; font-weight: 700;
    font-size: 32px; letter-spacing: 0.2px; white-space: nowrap;
  }
  .tier-label {
    font-family: "Arimo", sans-serif; font-weight: 700;
    font-size: 10px; line-height: 1.1;
  }

  .holder-fields {
    position: absolute; left: 76px; top: 305px;
    font-family: "Arimo", sans-serif; font-style: italic; font-weight: 400;
    font-size: 13px; color: var(--label-grey);
    display: grid; grid-template-columns: 38px auto; row-gap: 22px;
  }
</style>
</head>
<body>
<main class="stage">

  <section class="vip-card vip-card--gold" aria-label="Gold membership card">
    <div class="card-art" role="img" aria-label="Flowing rainbow wire-line waves sweeping across the card">
      <div class="art-band"></div>
      <div class="art-swirl"></div>
    </div>
    <div class="brand"><span class="brand-dot"></span><span class="brand-name">Velmora Spa</span></div>
    <div class="tier-ribbon">
      <span class="tier-name">EXCLUSIVE GOLD</span>
      <span class="tier-label">VIP<br>Card</span>
    </div>
    <div class="holder-fields">
      <span>Name</span><span>:</span>
      <span>ID</span><span>:</span>
    </div>
  </section>

  <section class="vip-card vip-card--silver" aria-label="Silver membership card">
    <div class="card-art" role="img" aria-label="Flowing rainbow wire-line waves sweeping across the card">
      <div class="art-band"></div>
      <div class="art-swirl"></div>
    </div>
    <div class="brand"><span class="brand-dot"></span><span class="brand-name">Velmora Spa</span></div>
    <div class="tier-ribbon">
      <span class="tier-name">EXCLUSIVE SILVER</span>
      <span class="tier-label">VIP<br>Card</span>
    </div>
    <div class="holder-fields">
      <span>Name</span><span>:</span>
      <span>ID</span><span>:</span>
    </div>
  </section>

</main>
</body>
</html>
```